Gerald Munro - Corporate MC & Entertainer

Design a one page A4 flyer
I'm after a one Page Flyer
A4 Size - One sided
I want the finished artwork in 2 Forms.
1/ One that I could print out myself in a small run ( I have a Vextra Colour PrintJet)
or send out as a PDF
2/ A second version that could be printed commercially , so including bleed crop marks so it can be cut to A4 size
I have attached the copy that should be included. (Podium Pulse 2014 WORDS)
If there was too much text to include , we could drop one of the testimonial quotes
I have attached 3 images that could be included if there is room.
If there were too many images I suggest dropping Image 3 ( with bow tie)
As you can see from the copy (or a visit to my website) there are two main services that I provide
Corporate MC Services and Entertainment Services.
These are however intertwined - My MC work often includes some entertaining effects from my ThoughtCatcher Act. I often get booked to MC a conference and provide a show.
I'm after something that is -
Classy , Sophisticated, Smart, perhaps a bit quirky.
Nothing "Magic" like - eg no Rabbits , Wands, puffs of smoke
I have no corporate colour or logo or branding that should be included
You can see some previous flyers here http://www.proflinknet.com/in/geraldmunro
I like these, but looking for new ideas
Target Market(s)
Corporate , Conference Organisers, Speaker Bureau owners, Large Association Conference committees
Industry/Entity Type
Entertainment
Colors
Designer to choose colors to be used in the design.
Look and feel

```html
<!DOCTYPE html>
<html lang="en">
<head>
<meta charset="utf-8">
<title>Gerald Munro – Corporate MC &amp; Entertainer</title>
<link href="https://fonts.googleapis.com/css2?family=Archivo:ital,wght@0,800;0,900;1,800;1,900&family=Questrial&family=Libre+Baskerville&display=swap" rel="stylesheet">
<style>
  :root {
    --page: #ffffff;
    --ink-black: #000000;
    --white: #ffffff;
    --gold-light: #fbe16a;
    --gold-deep: #eea43a;
    --orange: #f2a043;
    --band-top: #f6c64a;
    --band-bottom: #fde9a6;
    --photo-dark: #1c1c1c;
    --photo-mid: #4a4a4a;
  }
  * { margin: 0; padding: 0; box-sizing: border-box; }
  html, body { width: 1000px; height: 1200px; overflow: hidden; background: var(--page); }
  .flyer { position: relative; width: 1000px; height: 1200px; }
  .sheet { position: absolute; left: 76px; top: 0; width: 848px; height: 1200px; background: var(--ink-black); overflow: hidden; }
  .hero-photo {
    position: absolute; left: 0; top: 0; width: 848px; height: 516px;
    background:
      radial-gradient(ellipse 220px 260px at 220px 260px, rgba(210,190,170,0.55), transparent 70%),
      linear-gradient(160deg, var(--photo-mid) 0%, #2e2e2e 45%, var(--photo-dark) 100%);
  }
  .name {
    position: absolute; right: 40px; top: 80px; text-align: right;
    font-family: "Archivo", Arial, sans-serif; font-weight: 900; font-style: italic;
    font-size: 104px; line-height: 80px; letter-spacing: -2px;
    background: linear-gradient(180deg, var(--gold-light) 0%, var(--gold-deep) 100%);
    -webkit-background-clip: text; background-clip: text; color: transparent;
    padding-right: 6px;
  }
  .country {
    position: absolute; right: 30px; top: 420px;
    font-family: "Archivo", Arial, sans-serif; font-weight: 900;
    font-size: 68px; line-height: 70px; color: var(--white); letter-spacing: -1px;
    text-shadow: 0 2px 6px rgba(0,0,0,0.6);
  }
  .title {
    position: absolute; left: 212px; top: 486px;
    font-family: "Libre Baskerville", Georgia, serif; font-size: 44px; line-height: 56px;
    background: linear-gradient(180deg, var(--gold-light) 0%, var(--gold-deep) 100%);
    -webkit-background-clip: text; background-clip: text; color: transparent;
  }
  .tagline {
    position: absolute; left: 0; width: 848px; top: 561px; text-align: center;
    font-family: "Archivo", Arial, sans-serif; font-weight: 800; font-style: italic;
    font-size: 23.5px; color: var(--white); white-space: nowrap;
  }
  .rule { position: absolute; left: 20px; top: 603px; width: 808px; height: 2px; background: var(--white); }
  .bio {
    position: absolute; left: 49px; top: 648px; width: 750px; text-align: center;
    font-family: "Questrial", "Century Gothic", sans-serif; font-size: 16.5px; line-height: 23px; color: var(--white);
  }
  .bio p { margin-bottom: 23px; }
  .upcoming {
    position: absolute; left: 0; width: 848px; top: 930px; text-align: center;
    font-family: "Archivo", Arial, sans-serif; font-weight: 900; font-style: italic;
    font-size: 43px; color: var(--white); white-space: nowrap;
  }
  .cta {
    position: absolute; left: 0; width: 848px; top: 983px; text-align: center;
    font-family: "Archivo", Arial, sans-serif; font-weight: 800; font-size: 26.5px; color: var(--orange); white-space: nowrap;
  }
  .testimonials {
    position: absolute; left: 0; top: 1040px; width: 848px; height: 160px;
    background: linear-gradient(180deg, var(--band-top) 0%, var(--band-bottom) 100%);
    padding: 24px 22px 0 22px;
  }
  .testimonials h2 {
    display: flex; align-items: center; gap: 12px;
    font-family: "Archivo", Arial, sans-serif; font-weight: 800; font-size: 16px; color: var(--ink-black);
  }
  .testimonials h2::after { content: ""; flex: 0 0 606px; height: 3px; background: var(--ink-black); }
  .quote {
    margin-top: 16px; font-family: "Archivo", Arial, sans-serif; font-weight: 800;
    font-size: 11px; line-height: 19px; color: var(--ink-black);
  }
  .quote cite { font-style: normal; font-weight: 900; }
</style>
</head>
<body>
  <div class="flyer">
    <div class="sheet">
      <div class="hero-photo" role="img" aria-label="Photo of a smiling grey-haired presenter in a dark suit pointing upward beside conference microphones, in front of dark city skyscrapers"></div>
      <h1 class="name">Gerald<br>Munro</h1>
      <div class="country">AUSTRALIA'S</div>
      <div class="title">Conductor of&nbsp; the Mind</div>
      <p class="tagline">Corporate MC &nbsp;&amp;&nbsp; Entertainer. Solving your Conference Puzzles!</p>
      <div class="rule"></div>
      <div class="bio">
        <p>In the last two years Gerald has been engaged as the Conference MC for events in Hawaii, New Zealand, Hong Kong &amp; all States of Australia.</p>
        <p>He facilitated 24 Australian Major Project Conferences for Kestrova Expos and 16 International CEO Summits for Varnell Summits Intl.</p>
        <p>In the Australian Corporate Sector, he managed major events for &nbsp;- Quillbrook Brokers, Fennimore Cover, Halvencare, Rentavox, Ossory Care and the Greenvale Growers Guild.</p>
        <p>As an Entertainer he cruised the world on several luxury cruise ships, visiting Japan, Korea, China, Tahiti and New Zealand in his travels.</p>
      </div>
      <h2 class="upcoming">What's coming up in 2014?</h2>
      <p class="cta">Get involved at http://www.GeraldMunro.com</p>
      <section class="testimonials">
        <h2>Recent Testimonials</h2>
        <p class="quote">"A big thank you for a really good job on Friday night which was carried out with aplomb - &nbsp;well done!" &nbsp;<cite>- Greenvale Growers Guild</cite></p>
        <p class="quote">"Huge thanks for your professionalism with the Awards, getting a laugh from everyone and in general creating an atmosphere that was enjoyable and relaxed!" &nbsp;<cite>- Halvencare</cite></p>
      </section>
    </div>
  </div>
</body>
</html>
```